Brightstone Roofing Business Card

This is my current business card. But I’d like to make some changes. Somewhere on the card I’d like to list some of the services we offer. Maybe on the back? But I’d still like to keep the red. White and black modern look.

-residential & commercial roofing
-Roof Repairs & Maintenance
-Storm Damage & Insurance Claims specialist
-Christmas Lights and permanent Christmas lights
Fencing. Windows. Gutters. Siding. Sheetrock, painting.

```html
<!DOCTYPE html>
<html lang="en">
<head>
<meta charset="utf-8">
<title>Brightstone Roofing Co. – Business Card</title>
<link rel="stylesheet" href="https://fonts.googleapis.com/css2?family=Lato:wght@400;700;900&family=Michroma&display=swap">
<style>
  :root {
    --stage: #2c2c2c;
    --card-black: #050505;
    --red: #e21f26;
    --red-deep: #8e1015;
    --red-dark: #5e0a0d;
    --white: #ffffff;
    --grey-text: #e9e9e9;
  }
  * { box-sizing: border-box; margin: 0; padding: 0; }
  html, body { width: 1200px; height: 694px; overflow: hidden; }
  body {
    background: var(--stage);
    font-family: "Lato", Arial, sans-serif;
    position: relative;
  }
  .card {
    position: absolute;
    top: 192px;
    width: 540px;
    height: 309px;
    border-radius: 16px;
    overflow: hidden;
    box-shadow: 0 14px 30px rgba(0,0,0,.45);
  }
  .card--front { left: 40px; }
  .card--back { left: 620px; background: var(--card-black); }

  /* Front */
  .pattern-field {
    position: absolute; inset: 0;
    background: linear-gradient(135deg, var(--red-deep) 0%, var(--red) 45%, var(--red-deep) 75%, var(--red-dark) 100%);
  }
  .front-brand {
    position: absolute; inset: 0;
    display: flex; flex-direction: column; align-items: center; justify-content: center;
    gap: 14px;
  }
  .brand-dot {
    width: 96px; height: 96px; border-radius: 50%;
    background: var(--card-black);
    border: 4px solid var(--white);
  }
  .front-brand .brand-name {
    font-weight: 900;
    color: var(--white);
    font-size: 30px;
    letter-spacing: 2px;
    text-transform: uppercase;
    text-align: center;
    line-height: 1.05;
  }

  /* Back */
  .back-brand {
    position: absolute; left: 34px; top: 34px; width: 170px;
    display: flex; flex-direction: column; align-items: center; gap: 10px;
  }
  .back-brand .brand-dot { width: 72px; height: 72px; background: var(--red); border-color: var(--white); border-width: 3px; }
  .back-brand .brand-name {
    font-weight: 900; color: var(--red);
    font-size: 17px; letter-spacing: 1px; text-transform: uppercase;
    text-align: center; line-height: 1.1;
  }
  .divider {
    position: absolute; left: 220px; top: 28px; width: 2px; height: 128px;
    background: linear-gradient(180deg, transparent, var(--red) 20%, var(--red) 80%, transparent);
  }
  .contact { position: absolute; left: 240px; top: 30px; }
  .contact-name {
    font-family: "Michroma", "Lato", sans-serif;
    font-size: 19px; color: var(--white); letter-spacing: 1px;
    text-transform: uppercase; font-weight: 400;
  }
  .contact-name .first { color: var(--red); }
  .contact-role { color: var(--grey-text); font-size: 14px; margin: 3px 0 10px; }
  .contact-list { list-style: none; }
  .contact-list li {
    display: flex; align-items: center; gap: 8px;
    color: var(--white); font-size: 13.5px; margin-bottom: 6px;
  }
  .contact-list svg { width: 14px; height: 14px; flex: none; }

  .services {
    position: absolute; left: 34px; top: 178px; right: 24px;
    list-style: none; color: var(--white); font-size: 13px; line-height: 1.55;
  }
  .services .dot { color: var(--red); font-weight: 900; margin: 0 5px; }
  .services .dot:first-child { margin-left: 0; }

  .pattern-strip {
    position: absolute; left: 0; right: 0; bottom: 0; height: 30px;
    background: linear-gradient(90deg, var(--red-dark), var(--red) 50%, var(--red-dark));
  }
</style>
</head>
<body>

  <section class="card card--front" aria-label="Business card front">
    <div class="pattern-field" role="img" aria-label="Red, black and white tartan pattern background"></div>
    <div class="front-brand">
      <span class="brand-dot" aria-hidden="true"></span>
      <p class="brand-name">Brightstone<br>Roofing Co.</p>
    </div>
  </section>

  <section class="card card--back" aria-label="Business card back">
    <div class="back-brand">
      <span class="brand-dot" aria-hidden="true"></span>
      <p class="brand-name">Brightstone<br>Roofing Co.</p>
    </div>

    <div class="divider" aria-hidden="true"></div>

    <div class="contact">
      <h1 class="contact-name"><span class="first">Dylan</span> Marsh</h1>
      <p class="contact-role">Owner</p>
      <ul class="contact-list">
        <li>
          <svg viewBox="0 0 24 24" aria-hidden="true"><path fill="#e21f26" d="M6.6 10.8a15 15 0 0 0 6.6 6.6l2.2-2.2c.3-.3.7-.4 1-.2 1.1.4 2.3.6 3.6.6.6 0 1 .4 1 1V20c0 .6-.4 1-1 1A17 17 0 0 1 3 4c0-.6.4-1 1-1h3.5c.6 0 1 .4 1 1 0 1.3.2 2.5.6 3.6.1.3 0 .7-.2 1z"/></svg>
          555-013-2748
        </li>
        <li>
          <svg viewBox="0 0 24 24" aria-hidden="true"><path fill="#e21f26" d="M2 5h20v14H2z"/><path fill="none" stroke="#050505" stroke-width="2" d="M2 5l10 8 10-8"/></svg>
          Dylan@brightstoneroofing.co
        </li>
        <li>
          <svg viewBox="0 0 24 24" aria-hidden="true"><circle cx="12" cy="12" r="10" fill="#e21f26"/><path fill="none" stroke="#050505" stroke-width="1.5" d="M2 12h20M12 2c3 3 3 17 0 20M12 2c-3 3-3 17 0 20"/></svg>
          www.brightstoneroofing.co
        </li>
      </ul>
    </div>

    <ul class="services" aria-label="Services">
      <li><span class="dot">•</span>Residential &amp; commercial roofing <span class="dot">•</span>Roof Repairs &amp; Maintenance</li>
      <li><span class="dot">•</span>Storm Damage &amp; Insurance Claims specialist</li>
      <li><span class="dot">•</span>Christmas Lights and permanent Christmas lights</li>
      <li><span class="dot">•</span>Fencing <span class="dot">•</span>Windows <span class="dot">•</span>Gutters <span class="dot">•</span>Siding <span class="dot">•</span>Sheetrock <span class="dot">•</span>Painting</li>
    </ul>

    <div class="pattern-strip" role="img" aria-label="Red tartan pattern strip"></div>
  </section>

</body>
</html>
```